The Founder Crossroads Book Cover

I need a Book Cover Design for a new book:
Title - "The Founder Crossroads"
Subtitle - "Lessons No Classroom Ever Gives You"
Author - "Marcus Halden"

Target Market(s)

Entrepreneur's and Small Business Owners

Industry/Entity Type

Entrepreneur

Font styles to use
Sans Serif

Requirements
Must have
• The branding colors should match our website (Black and accent color: #FBBC05)
• http://FounderCrossroads.example
• Secondary Subtile (top bar) on front of cover - "A Documentary"
• Back Cover: Brief description, author photo, and the ISBN Number
Nice to have
• A Detour Sign with the word "Detour" on it (or a sign with a "squiggly" line example) ... or a type of image that is on the bottom of Home page of website (road in wilderness).

```html
<!DOCTYPE html>
<html lang="en">
<head>
<meta charset="UTF-8">
<title>The Founder Crossroads — Book Cover</title>
<link rel="stylesheet" href="https://fonts.googleapis.com/css2?family=Roboto:wght@300;400;700;900&display=swap">
<style>
  :root {
    --ink: #000000;
    --paper: #ffffff;
    --accent: #fbbc05;
    --rule: #8c8c8c;
    --sky: #eef3f4;
    --mountain: #8fb0c0;
    --sand: #d2aa78;
    --dust: #a9835a;
    --road: #2a2119;
  }
  * { box-sizing: border-box; margin: 0; padding: 0; }
  html, body {
    width: 774px;
    height: 1200px;
    overflow: hidden;
    background: var(--ink);
  }
  .cover {
    position: relative;
    width: 774px;
    height: 1200px;
    background: var(--ink);
    font-family: "Roboto", Arial, sans-serif;
    color: var(--paper);
    overflow: hidden;
  }
  .cover-photo {
    position: absolute;
    inset: 0 0 auto 0;
    height: 800px;
    background:
      linear-gradient(180deg,
        var(--sky) 0%,
        #e3ecef 5%,
        var(--mountain) 12%,
        #b9b3a0 17%,
        var(--sand) 22%,
        var(--dust) 34%,
        #5a4331 44%,
        var(--road) 56%,
        #17120e 78%,
        var(--ink) 100%);
  }
  .title-block {
    position: absolute;
    left: 0;
    right: 0;
    top: 624px;
    text-align: center;
    font-weight: 700;
    line-height: 1;
  }
  .title-lead {
    display: block;
    font-size: 66px;
    letter-spacing: -1px;
  }
  .title-main {
    display: block;
    margin-top: 10px;
    font-size: 64px;
    letter-spacing: -1.5px;
    white-space: nowrap;
  }
  .title-main .accent { color: var(--accent); }
  .divider {
    position: absolute;
    left: 126px;
    width: 522px;
    height: 24px;
    display: flex;
    align-items: center;
    gap: 6px;
  }
  .divider::before,
  .divider::after {
    content: "";
    flex: 1;
    height: 1px;
    background: var(--rule);
  }
  .divider-mark {
    width: 96px;
    height: 14px;
    background: var(--paper);
    opacity: 0.85;
    border-radius: 7px;
  }
  .divider--top { top: 854px; }
  .divider--bottom { top: 1012px; }
  .subtitle {
    position: absolute;
    left: 170px;
    width: 434px;
    top: 904px;
    text-align: center;
    font-weight: 300;
    font-size: 30px;
    line-height: 46px;
    letter-spacing: 0.5px;
  }
  .byline {
    position: absolute;
    left: 0;
    right: 0;
    top: 1094px;
    text-align: center;
    font-size: 30px;
    font-weight: 400;
  }
  .byline .author {
    color: var(--accent);
    font-weight: 900;
  }
</style>
</head>
<body>
  <main class="cover">
    <div class="cover-photo" role="img" aria-label="Photograph of a long desert highway stretching toward distant mountains under a pale sky"></div>

    <h1 class="title-block">
      <span class="title-lead">The</span>
      <span class="title-main"><span class="accent">FOUNDER</span> CROSSROADS</span>
    </h1>

    <div class="divider divider--top"><span class="divider-mark" role="img" aria-label="Decorative flourish"></span></div>

    <p class="subtitle">Lessons No Classroom Ever Gives You</p>

    <div class="divider divider--bottom"><span class="divider-mark" role="img" aria-label="Decorative flourish"></span></div>

    <p class="byline">by <span class="author">Marcus Halden</span></p>
  </main>
</body>
</html>
```